Zestbite Site

I would like to do a blog for food lovers. The name of the blog is BiteZest. I want to build something like Marcus Fennimore and Tobias Wrenfield. Something cool and different. In this blog i need: Place for pictures, videos, instagram connection, Facebook Linked to see fans wich like the blog on Facebook....

Reason: I need more options of design.

Requirements
Nice to have
• - Facebook link
- Instagram
- Something with foursquare

```html
<!DOCTYPE html>
<html lang="en">
<head>
<meta charset="utf-8">
<title>Zestbite</title>
<link href="https://fonts.googleapis.com/css2?family=Open+Sans:wght@400;600;700&family=Raleway:wght@300&display=swap" rel="stylesheet">
<style>
:root{
  --green:#7cb83a;
  --green-dark:#5a9a28;
  --teal:#2a9a9a;
  --red:#d8323a;
  --link:#2a8fc0;
  --ink:#333;
  --muted:#777;
  --line:#cfd3d4;
  --page:#eef0f1;
  --panel:#e6e8e9;
  --footer:#2b2b2b;
  --blue:#2a96d6;
}
*{box-sizing:border-box;margin:0;padding:0}
html,body{width:1200px;height:2190px;overflow:hidden}
body{position:relative;background:var(--page);font-family:"Open Sans",Arial,sans-serif;color:var(--ink)}
.abs{position:absolute}
.header{left:0;top:0;width:1200px;height:180px;background:linear-gradient(#fff,#f1f2f2);border-bottom:1px solid #ddd}
.brand{left:166px;top:22px;width:140px;text-align:center}
.brand-mark{width:56px;height:56px;border-radius:50%;background:var(--green);margin:0 auto 12px}
.brand-name{font-family:"Raleway",sans-serif;font-weight:300;font-size:40px;letter-spacing:1px;color:#777;line-height:1}
.toplinks{right:130px;top:20px;font-size:12px;color:#444;display:flex;gap:10px;align-items:center}
.flag{width:24px;height:14px;background:#3a4f8c;display:inline-block;border:1px solid #ccc}
.search{left:802px;top:74px;width:268px;height:36px;border:1px solid #ccc;border-radius:18px;background:#fff;font-size:12px;color:#aaa;font-style:italic;padding:9px 14px}
.search-btn{left:1028px;top:69px;width:42px;height:42px;border-radius:50%;background:var(--blue);border:3px solid #fff;box-shadow:0 0 0 1px #9cc}
.nav{left:492px;top:124px;display:flex;align-items:center;font-size:15px;color:#333}
.nav a{padding:0 16px;border-right:1px solid #ccc;line-height:22px;color:#333;text-decoration:none}
.nav a:last-child{border:none}
.nav a.active{background:var(--green);color:#fff;border:none;line-height:39px;padding:0 21px;border-radius:3px;margin-right:8px}
.hero{left:0;top:180px;width:1200px;height:426px;background:linear-gradient(110deg,#c9b89a 0%,#e8e2d6 35%,#f3ece3 55%,#c79a6a 100%)}
.post-head{left:130px;width:620px;height:62px;border-top:2px solid var(--line);border-bottom:1px solid var(--line)}
.post-title{position:absolute;left:15px;top:10px;font-size:16px;font-weight:600;color:#333}
.post-date{position:absolute;left:15px;top:36px;font-size:11px;font-style:italic;color:#888}
.share{position:absolute;right:4px;top:20px;display:flex;gap:6px;align-items:center;font-size:11px}
.pill{border:1px solid #bbb;border-radius:3px;background:#fff;padding:1px 7px;color:#345}
.count{border:1px solid #ccc;background:#fff;padding:1px 5px;color:#555}
.insta{width:20px;height:20px;background:#6b4e3b;border-radius:3px;margin-left:10px}
.media{left:130px;width:620px;border:1px solid #ccc}
.likes{left:130px;width:620px;background:var(--panel);padding:16px 15px}
.likes-count{font-size:12px;color:var(--red);margin-bottom:14px}
.comment{display:flex;gap:12px;padding:8px 4px;border-bottom:2px solid var(--page);height:74px}
.avatar{width:44px;height:44px;background:#333;flex:none}
.c-name{font-size:12px;font-weight:700;color:var(--teal)}
.c-text{font-size:12px;color:#555}
.c-meta{font-size:10px;color:#555;margin-top:6px}
.c-meta span{color:var(--red)}
.write{margin-top:10px;height:22px;border:1px solid #ccc;background:#fff;font-size:10px;color:#888;padding:3px 8px}
.play{left:395px;top:1434px;width:84px;height:84px;border-radius:50%;background:rgba(40,140,200,.85);border:4px solid rgba(255,255,255,.6)}
.pager{left:210px;top:1878px;width:460px;display:flex;align-items:center;font-size:15px;color:var(--link)}
.pager span{padding:0 16px;border-right:1px solid #aaa;line-height:16px}
.pager span:nth-last-child(2){border:none}
.pager .cur{color:#333}
.side-head{left:800px;width:270px;height:46px;border-top:1px solid var(--line);border-bottom:1px solid var(--line);font-size:19px;font-weight:600;padding:9px 0 0 0;color:#333}
.thumb{width:128px;height:94px;border:2px solid #c53a4a;border-radius:4px;background:linear-gradient(#e7c3a0,#cf7d45 60%,#f4f0ea)}
.caption{width:128px;text-align:center;font-size:12px;color:#333}
.list{left:800px;width:270px;list-style:none;font-size:13px;color:#333}
.list li{position:relative;padding-left:22px;height:32px;line-height:20px}
.list li::before{content:"";position:absolute;left:2px;top:5px;border-left:8px solid var(--green);border-top:5px solid transparent;border-bottom:5px solid transparent}
.list li.more{font-weight:700}
.ad{left:769px;top:1023px;width:301px;height:251px;border:4px solid #5aa83a;background:#fff;overflow:hidden}
.ad-top{height:58px;background:linear-gradient(#fff,#e8e8e8);font-size:20px;color:#333;padding:12px 0 0 14px;display:flex;align-items:center;gap:8px}
.ad-top i{width:22px;height:26px;background:#5aa83a;display:inline-block}
.ad-title{position:absolute;left:12px;top:62px;font-size:21px;font-weight:700;color:#111;line-height:1.1}
.ad-sub{position:absolute;left:12px;top:88px;font-size:14px;font-weight:600;color:#222}
.ad-price{position:absolute;left:12px;top:138px;width:88px;height:38px;background:#f09a1a;color:#3a1a00;font-weight:700;font-size:17px;padding:7px 10px;transform:rotate(-6deg)}
.ad-prod{position:absolute;left:160px;top:82px;width:116px;height:110px;background:linear-gradient(135deg,#333,#0a0a0a)}
.ad-foot{position:absolute;left:10px;bottom:6px;font-size:9px;font-weight:700;color:#222;display:flex;gap:14px}
.ad-buy{position:absolute;right:8px;bottom:4px;background:var(--red);color:#fff;font-weight:700;font-size:17px;padding:3px 14px}
.footer{left:0;top:1953px;width:1200px;height:237px;background:var(--footer);color:#ddd}
.f-col{position:absolute;top:32px;width:220px}
.f-col h4{font-size:14px;font-weight:700;color:#fff;margin-bottom:12px}
.f-col p{font-size:12px;height:31px;color:#ddd}
.social{position:absolute;left:855px;top:30px;display:flex;gap:10px}
.social i{width:30px;height:30px;border-radius:50%;background:#555;display:block}
.f-logo{position:absolute;left:855px;top:99px;width:110px;height:79px;background:#fff;display:flex;align-items:center;justify-content:center;font-family:"Raleway",sans-serif;font-weight:300;font-size:16px;color:#777}
.copy{position:absolute;left:855px;top:196px;font-size:11px;line-height:19px}
</style>
</head>
<body>

<header class="abs header">
  <div class="abs brand"><div class="brand-mark"></div><div class="brand-name">ZESTBITE</div></div>
  <div class="abs toplinks">Select Country : <i class="flag" role="img" aria-label="Country flag"></i> | <span>Login</span> | <span>Newsletter</span></div>
  <div class="abs search">Search</div>
  <div class="abs search-btn"><svg width="36" height="36" viewBox="0 0 36 36"><circle cx="20" cy="16" r="6" fill="none" stroke="#fff" stroke-width="3"/><line x1="15" y1="21" x2="10" y2="26" stroke="#fff" stroke-width="4" stroke-linecap="round"/></svg></div>
  <nav class="abs nav"><a class="active">Home</a><a>About Zestbite</a><a>News</a><a>Store</a><a>Blog Post</a><a>Contact</a></nav>
</header>

<div class="abs hero" role="img" aria-label="Close-up photo of fresh rice paper spring rolls on a plate"></div>

<!-- Post one -->
<div class="abs post-head" style="top:643px">
  <div class="post-title">Fusce quis lorem sem, sed adipiscing arcu.</div>
  <div class="post-date">Posted on 2hrs ago</div>
  <div class="share"><span class="pill">Like</span><span class="count">3k</span><span class="pill">Post</span><span class="count">318</span><i class="insta"></i></div>
</div>
<div class="abs media" style="top:718px;height:295px;background:linear-gradient(120deg,#e7efe0,#8c5a3a 45%,#d5472e 70%,#f3f3ef)" role="img" aria-label="Photo of grilled beef salad with tomatoes and greens"></div>
<div class="abs likes" style="top:1016px;height:219px">
  <div class="likes-count">3 people likes this</div>
  <div class="comment"><div class="avatar"></div><div><div class="c-text"><span class="c-name">Robin Harlow</span> Under the watchful eye of Newcastle</div><div class="c-meta">Yesterdat at 10pm. <span>Like</span></div></div></div>
  <div class="comment" style="border:none;height:62px"><div class="avatar"></div><div><div class="c-text"><span class="c-name">Robin Harlow</span> Under the watchful eye of Newcastle</div><div class="c-meta">Yesterdat at 10pm. <span>Like</span></div></div></div>
  <div class="write">Write a Comments.......</div>
</div>

<!-- Post two -->
<div class="abs post-head" style="top:1252px;border-bottom:none">
  <div class="post-title">Fusce quis lorem sem, sed adipiscing arcu.</div>
  <div class="post-date">Posted on 2hrs ago</div>
  <div class="share"><span class="pill">Like</span><span class="count">3k</span><span class="pill">Post</span><span class="count">316</span><i class="insta"></i></div>
</div>
<div class="abs media" style="top:1326px;height:296px;background:linear-gradient(#1c1a18,#3a302a 60%,#8a8580)" role="img" aria-label="Video still of a team of chefs in a restaurant kitchen"></div>
<div class="abs play"><svg width="76" height="76" viewBox="0 0 76 76"><polygon points="28,20 58,38 28,56" fill="#fff"/></svg></div>
<div class="abs likes" style="top:1626px;height:217px">
  <div class="likes-count">3 people likes this</div>
  <div class="comment"><div class="avatar"></div><div><div class="c-text"><span class="c-name">Robin Harlow</span> Under the watchful eye of Newcastle</div><div class="c-meta">Yesterdat at 10pm. <span>Like</span></div></div></div>
  <div class="comment" style="border:none;height:62px"><div class="avatar"></div><div><div class="c-text"><span class="c-name">Robin Harlow</span> Under the watchful eye of Newcastle</div><div class="c-meta">Yesterdat at 10pm. <span>Like</span></div></div></div>
  <div class="write">Write a Comments.......</div>
</div>

<div class="abs pager">
  <svg width="16" height="20" viewBox="0 0 16 20" style="margin-right:8px"><polyline points="12,2 4,10 12,18" fill="none" stroke="#555" stroke-width="3"/></svg>
  <span class="cur">1</span><span>2</span><span>3</span><span>4</span><span>5</span><span>6</span><span>7</span><span>8</span><span>9</span>
  <svg width="16" height="20" viewBox="0 0 16 20"><polyline points="4,2 12,10 4,18" fill="none" stroke="#555" stroke-width="3"/></svg>
</div>

<!-- Sidebar -->
<div class="abs side-head" style="top:643px">Popular</div>
<div class="abs thumb" style="left:800px;top:706px" role="img" aria-label="Photo of a pasta dish"></div>
<div class="abs thumb" style="left:942px;top:706px" role="img" aria-label="Photo of a pasta dish"></div>
<div class="abs caption" style="left:800px;top:808px">lorem sem, sed</div>
<div class="abs caption" style="left:942px;top:808px">lorem sem, sed</div>
<div class="abs thumb" style="left:800px;top:860px" role="img" aria-label="Photo of a pasta dish"></div>
<div class="abs thumb" style="left:942px;top:860px" role="img" aria-label="Photo of a pasta dish"></div>
<div class="abs caption" style="left:800px;top:968px">lorem sem, sed</div>
<div class="abs caption" style="left:942px;top:968px">lorem sem, sed</div>

<div class="abs ad">
  <div class="ad-top"><i></i>Cartwell.com</div>
  <div class="ad-title">Norvik DataStick</div>
  <div class="ad-sub">4GB Pen Drive</div>
  <div class="ad-price">Rs.299</div>
  <div class="ad-prod" role="img" aria-label="Product photo of two black pen drives"></div>
  <div class="ad-foot"><span>FREE<br>SHIPPING</span><span>CASH ON<br>DELIVERY</span></div>
  <div class="ad-buy">Buy Now</div>
</div>

<div class="abs side-head" style="top:1299px">Categories</div>
<ul class="abs list" style="top:1362px">
  <li>At vero eos et accusamus et</li>
  <li>Iusto odio digmos sucimus qui</li>
  <li>Blanditiis praesentium deleniti</li>
  <li>Atque corrupti quos dolores et</li>
  <li class="more">View All</li>
</ul>

<div class="abs side-head" style="top:1558px">Archives</div>
<ul class="abs list" style="top:1621px">
  <li>May 2012</li>
  <li>April 2012</li>
  <li>March 2012</li>
  <li>April 2012</li>
  <li class="more">View All</li>
</ul>

<footer class="abs footer">
  <div class="f-col" style="left:130px"><h4>Zestbite</h4><p>At vero eos et accusamus et</p><p>Iusto odio digmos sucimus qui</p><p>Blanditiis praesentium deleniti</p><p>Atque corrupti quos dolores et</p></div>
  <div class="f-col" style="left:368px"><h4>Restaurants</h4><p>At vero eos et accusamus et</p><p>Iusto odio digmos sucimus qui</p><p>Blanditiis praesentium deleniti</p><p>Atque corrupti quos dolores et</p></div>
  <div class="f-col" style="left:610px"><h4>Shop</h4><p>At vero eos et accusamus et</p><p>Iusto odio digmos sucimus qui</p><p>Blanditiis praesentium deleniti</p><p>Atque corrupti quos dolores et</p></div>
  <div class="social"><i></i><i></i><i></i><i></i><i></i></div>
  <div class="f-logo">ZESTBITE</div>
  <div class="copy">Copyright © 2012 All Rights Reserved<br>Privacy Policy</div>
</footer>

</body>
</html>
```